Design main and detail pages for travel security app on Kestrova

I need of a new design for restyling of my travel security app for Kestrova. The new style has to be studied for models 4627, 4795 and newer.
You can see the actual style from the screenshots attached. You cannot change the style of "Vor" red box and "Logo" box because are both logos but you can change their position on the screen.
Menu.gif is the main screen when the user open the app. Travels.gif is the screen opened when the user click on "Travels" from main screen.
Travel_advice.gif is the screen opened clicking on "travel advices".
Travel_advice_detail.gif is the screen opened clicking on the name of a country listed on Travel_advice.gif screen.
Finally, I need of .psd file, icons, css (if necessary) and all necessary to implement the winner proposal.
menu.gif here: https://www.filquarro.com/s/pz41mqr8tvnw2ye/1_menu.gif
Travels.gif here: https://www.filquarro.com/s/hw28kdvnzq5trla/2_travels.gif
Travel_advice_detail.gif here: https://www.filquarro.com/s/ur63bxlmpw7jnc4/travel_advice_detail.gif
Travel_advice.gif here: https://www.filquarro.com/s/qe52ncvyrk8hdol/travel_advice.gif

```html
<!DOCTYPE html>
<html lang="en">
<head>
<meta charset="utf-8">
<title>Vor Travels Screen</title>
<link rel="stylesheet" href="https://fonts.googleapis.com/css2?family=Open+Sans:wght@600;700;800&family=Roboto+Condensed:wght@700&display=swap">
<style>
  :root {
    --red: #e3171b;
    --red-light: #f23a35;
    --red-dark: #c40f12;
    --blue-core: #1b7cc4;
    --blue-mid: #135d9c;
    --blue-edge: #0a355f;
    --ring: #050505;
    --white: #ffffff;
    --label: #333333;
  }
  * { margin: 0; padding: 0; box-sizing: border-box; }
  html, body { width: 1200px; height: 1200px; overflow: hidden; }
  body {
    position: relative;
    background: radial-gradient(circle at 50% 55%, var(--blue-core) 0%, var(--blue-mid) 45%, var(--blue-edge) 100%);
    font-family: "Open Sans", Arial, sans-serif;
  }
  .status-bar {
    position: absolute; left: 0; top: 0; width: 1200px; height: 126px;
    background: linear-gradient(180deg, var(--red-light) 0%, var(--red) 55%, var(--red-dark) 100%);
    border-bottom: 6px solid #f6f6f6;
    color: var(--white);
    z-index: 2;
  }
  .status-bar .brand-logo {
    position: absolute; left: 54px; top: 18px;
    font-size: 68px; font-weight: 800; letter-spacing: 1px;
  }
  .status-bar .brand-name {
    position: absolute; left: 684px; top: 18px;
    font-size: 68px; font-weight: 800; letter-spacing: 1px;
  }
  .status-bar .clock {
    position: absolute; left: 900px; top: 30px;
    display: flex; align-items: center; gap: 18px;
    font-size: 58px; font-weight: 600;
  }
  .status-bar .clock svg { width: 72px; height: 72px; }
  .menu-wheel { position: absolute; left: 0; top: 0; width: 1200px; height: 1200px; z-index: 1; }
  .wheel-label {
    font-family: "Roboto Condensed", "Arial Narrow", sans-serif;
    font-weight: 700; font-size: 52px; fill: var(--label);
  }
</style>
</head>
<body>
  <header class="status-bar">
    <div class="brand-logo">LOGO</div>
    <div class="brand-name">VOR</div>
    <div class="clock">
      <svg viewBox="0 0 24 24" aria-hidden="true">
        <circle cx="12" cy="12" r="9.5" fill="none" stroke="#fff" stroke-width="2.6"/>
        <path d="M12 6.5V12h4.5" fill="none" stroke="#fff" stroke-width="2.6" stroke-linecap="round"/>
      </svg>
      <span>13:13</span>
    </div>
  </header>

  <svg class="menu-wheel" viewBox="0 0 1200 1200" aria-label="Travels menu">
    <circle cx="615" cy="708" r="506" fill="var(--ring)"/>
    <circle cx="615" cy="708" r="390" fill="none" stroke="var(--white)" stroke-width="6"/>
    <circle cx="615" cy="708" r="276" fill="var(--white)"/>

    <g class="plane" fill="var(--red)" transform="translate(615 618) scale(0.9 0.8) translate(-625 -682)">
      <path d="M455 655 L505 655 L545 690 L660 640 L735 590 Q775 560 795 575 Q805 595 770 625 L700 670 L690 790 L655 805 L640 700 L560 740 L555 775 L530 785 L520 745 L445 690 Z"/>
      <path d="M560 585 L590 580 L665 635 L630 650 Z"/>
    </g>
    <text class="wheel-label" x="618" y="800" text-anchor="middle">TRAVELS</text>

    <g class="wheel-item">
      <circle cx="648" cy="302" r="100" fill="var(--white)"/>
      <path d="M628 248a34 34 0 0 1 34 34c0 26-34 74-34 74s-34-48-34-74a34 34 0 0 1 34-34z" fill="var(--red)"/>
      <circle cx="628" cy="282" r="14" fill="var(--white)"/>
      <path d="M682 254a22 22 0 0 1 22 22c0 17-22 48-22 48s-22-31-22-48a22 22 0 0 1 22-22z" fill="var(--red)" stroke="var(--white)" stroke-width="4"/>
      <circle cx="682" cy="276" r="9" fill="var(--white)"/>
    </g>

    <g class="wheel-item">
      <circle cx="216" cy="642" r="100" fill="var(--white)"/>
      <path d="M170 605h92a14 14 0 0 1 14 14v52a14 14 0 0 1-14 14h-52l-30 26v-26h-10a14 14 0 0 1-14-14v-52a14 14 0 0 1 14-14z" fill="var(--red)"/>
      <rect x="211" y="617" width="12" height="38" rx="4" fill="var(--white)"/>
      <circle cx="217" cy="670" r="7" fill="var(--white)"/>
    </g>

    <g class="wheel-item">
      <circle cx="994" cy="642" r="100" fill="var(--white)"/>
      <ellipse cx="994" cy="636" rx="56" ry="40" fill="var(--red)"/>
      <path d="M960 660 L948 700 L990 672 Z" fill="var(--red)"/>
    </g>

    <g class="wheel-item">
      <circle cx="615" cy="1014" r="100" fill="var(--white)"/>
      <circle cx="615" cy="1014" r="52" fill="var(--red)"/>
      <g fill="none" stroke="var(--white)" stroke-width="5">
        <ellipse cx="615" cy="1014" rx="22" ry="52"/>
        <line x1="563" y1="1014" x2="667" y2="1014"/>
        <path d="M572 988h86M572 1040h86"/>
      </g>
    </g>
  </svg>
</body>
</html>
```